Bargo Finch

I want a design for a website where users can insert products URLs from different sites and the user will get notified by email when that product's price changes.

On the homepage I'd like a big input where the user can insert a product's URL. On the same page the following will appear:
- my products that I follow (options: share, buy, unfollow) + it's current price and deviation from last time it's price has changed (I may have many products that I follow, so maybe a table layout would be wise. - just a suggestion)
- products that other people follow (options: follow). If my Chatterloop friends follow a certain product, I can see their photo(eg: friend1, friend2 and 5 others are following this product) (also, may people may follow a product.)

On the login page I can register using user / pass or using Chatterloop

The 3rd page is the product's page. Once I click on any product I go to this page. On this page I can see:
- picture, name and price and no of people following this product
- a chart with the product's price over the last 30 days
- list with friends that follow this product (when logged in)
- product options: follow / unfollow, share, buy

Then I want the design for an email template that I send when 1 or more prices of a user's products change.

Nice to have: want level for product - describes how much wanted is a product after a certain internal algorithm

NB:
- flat design (not really kestra, something more like the new Vyra interface - just a suggestion)
- I'd prefer a red theme (based on the idea that the site will be represented by a rooster)
- don't forget the design for basic elements: loading screen, popup, alert, messages, etc

I've posted an initial prototype with what I'd like the design to contain.

• - flat design
- must be simple. much white space
• as few gradients as possible

```html
<!DOCTYPE html>
<html lang="en">
<head>
<meta charset="utf-8">
<title>Bargo Finch</title>
<link rel="stylesheet" href="https://fonts.googleapis.com/css2?family=Source+Sans+3:wght@400;600;700&display=swap">
<style>
  :root {
    --red: #d0202e;
    --grey: #a9a9a9;
    --grey-light: #ececec;
    --line: #e2e2e2;
    --text: #1f1f1f;
    --muted: #7a7a7a;
    --white: #ffffff;
  }
  * { box-sizing: border-box; }
  html, body {
    margin: 0;
    width: 1145px;
    height: 1200px;
    overflow: hidden;
    background: var(--white);
    font-family: "Source Sans 3", Arial, sans-serif;
    color: var(--text);
  }
  .page { width: 947px; margin-left: 99px; }

  .site-header {
    margin-top: 32px; height: 34px;
    display: flex; justify-content: space-between; align-items: center;
  }
  .social { display: flex; gap: 14px; font-size: 14px; color: var(--grey); font-weight: 600; }
  .main-nav { display: flex; align-items: center; font-size: 14px; }
  .main-nav a { color: var(--text); text-decoration: none; }
  .main-nav .nav-home {
    background: var(--red); color: var(--white);
    width: 71px; height: 34px; display: flex; align-items: center; justify-content: center;
    margin-right: 44px;
  }
  .main-nav .nav-browse { margin-right: 52px; }
  .main-nav .nav-contact { margin-right: 2px; }

  .search-row { margin-top: 34px; height: 77px; display: flex; }
  .brand {
    width: 164px; background: var(--red); color: var(--white);
    display: flex; align-items: center; justify-content: center;
    font-size: 22px; font-weight: 600;
  }
  .follow-form {
    width: 618px; margin-left: 3px; background: var(--grey);
    padding: 10px 8px; display: flex;
  }
  .follow-form .url-input {
    flex: 1; background: var(--white); border: 1px solid #cfcfcf; border-right: none;
    display: flex; align-items: center; padding-left: 19px;
    font-size: 16px; color: var(--muted);
  }
  .follow-form .follow-btn {
    width: 120px; background: #f2f2f2; border: 1px solid #cfcfcf;
    display: flex; align-items: center; justify-content: center;
    font-size: 17px; font-weight: 600; color: #333;
  }
  .login-btn {
    width: 152px; margin-left: 5px; background: var(--grey); color: var(--white);
    display: flex; align-items: center; justify-content: center; font-size: 16px;
  }

  .section-title { margin: 26px 0 0; font-size: 21px; line-height: 24px; font-weight: 700; }
  .section-title.second { margin-top: 29px; }

  .product-grid { display: flex; gap: 13px; margin-top: 26px; }
  .product-grid.second { margin-top: 32px; }
  .product-card {
    width: 227px; height: 283px; border: 1px solid var(--line);
    padding: 24px 0 0 32px;
  }
  .product-grid.second .product-card { height: 289px; }
  .product-photo { width: 163px; height: 129px; display: block; }
  .product-name {
    width: 163px; margin-top: 13px; text-align: center;
    font-size: 12.5px; line-height: 16px;
  }
  .price-row { display: flex; gap: 3px; margin-top: 15px; height: 27px; font-size: 12.5px; color: var(--white); }
  .price-now { width: 78px; background: var(--red); display: flex; align-items: center; justify-content: center; }
  .price-change { width: 81px; background: var(--grey); display: flex; align-items: center; justify-content: center; gap: 6px; }
  .action-row {
    width: 163px; margin-top: 16px; height: 14px;
    display: flex; align-items: center; justify-content: space-between;
    font-size: 10px; color: var(--grey); font-weight: 600;
  }
  .share-group { display: flex; align-items: center; gap: 5px; }

  .followers { display: flex; gap: 4px; margin: 16px 0 0 -21px; }
  .follower { width: 48px; text-align: center; }
  .avatar { width: 48px; height: 48px; display: block; }
  .follower-name { font-size: 9px; color: var(--muted); margin-top: 4px; }
  .more-count {
    width: 48px; height: 48px; background: var(--grey-light);
    display: flex; align-items: center; justify-content: center; font-size: 12.5px;
  }

  .load-more {
    margin-top: 28px; height: 57px; background: var(--grey-light);
    display: flex; align-items: center; justify-content: center;
    font-size: 16px; color: #9a9a9a;
  }
  .load-more.second { height: 58px; }

  .site-footer {
    margin-top: 40px; border-top: 1px solid #d6d6d6; padding-top: 28px;
    text-align: center; font-size: 12px; line-height: 16px; color: #333;
  }
  .site-footer .divider { margin: 0 6px; }
  .site-footer a { color: var(--red); text-decoration: none; }
</style>
</head>
<body>
<div class="page">
  <header class="site-header">
    <div class="social"><span>Chatterloop</span><span>Wrenly</span></div>
    <nav class="main-nav">
      <a class="nav-home" href="#">Home</a>
      <a class="nav-browse" href="#">Browse Products</a>
      <a class="nav-contact" href="#">Contact</a>
    </nav>
  </header>

  <div class="search-row">
    <div class="brand">Bargo Finch</div>
    <div class="follow-form">
      <div class="url-input">Enter a product’s url</div>
      <div class="follow-btn">Follow</div>
    </div>
    <div class="login-btn">Login / Register</div>
  </div>

  <h2 class="section-title">My Products</h2>
  <div class="product-grid">
    <article class="product-card">
      <div class="product-photo" role="img" aria-label="Photo of wooden pencils with gold tips" style="background:#e6e4e0"></div>
      <div class="product-name">Special wood pencils</div>
      <div class="price-row"><span class="price-now">450 USD</span><span class="price-change">+4 USD <span>↑</span></span></div>
      <div class="action-row">
        <span class="share-group">Wrenly <svg width="13" height="12" viewBox="0 0 13 12"><rect x="0.5" y="0.5" width="9" height="11" fill="none" stroke="#a9a9a9"/><path d="M4 6h8M9 3l3 3-3 3" fill="none" stroke="#a9a9a9"/></svg></span>
        <span>BUY</span>
      </div>
    </article>
    <article class="product-card">
      <div class="product-photo" role="img" aria-label="Photo of a grey draped dress" style="background:#d9d3c9"></div>
      <div class="product-name">Modern dress with laces</div>
      <div class="price-row"><span class="price-now">450 USD</span><span class="price-change">+4 USD <span>↑</span></span></div>
      <div class="action-row">
        <span class="share-group">Wrenly <svg width="13" height="12" viewBox="0 0 13 12"><rect x="0.5" y="0.5" width="9" height="11" fill="none" stroke="#a9a9a9"/><path d="M4 6h8M9 3l3 3-3 3" fill="none" stroke="#a9a9a9"/></svg></span>
        <span>BUY</span>
      </div>
    </article>
    <article class="product-card">
      <div class="product-photo" role="img" aria-label="Photo of a stack of white pillows" style="background:#e8e8e8"></div>
      <div class="product-name">Set of pilows</div>
      <div class="price-row"><span class="price-now">450 USD</span><span class="price-change">+4 USD <span>↑</span></span></div>
      <div class="action-row">
        <span class="share-group">Wrenly <svg width="13" height="12" viewBox="0 0 13 12"><rect x="0.5" y="0.5" width="9" height="11" fill="none" stroke="#a9a9a9"/><path d="M4 6h8M9 3l3 3-3 3" fill="none" stroke="#a9a9a9"/></svg></span>
        <span>BUY</span>
      </div>
    </article>
    <article class="product-card">
      <div class="product-photo" role="img" aria-label="Photo of a gold plated cuff bracelet" style="background:linear-gradient(#efeeec,#e4e2de)"></div>
      <div class="product-name">Gold plated vintage breclet</div>
      <div class="price-row"><span class="price-now">450 USD</span><span class="price-change">+4 USD <span>↑</span></span></div>
      <div class="action-row">
        <span class="share-group">Wrenly <svg width="13" height="12" viewBox="0 0 13 12"><rect x="0.5" y="0.5" width="9" height="11" fill="none" stroke="#a9a9a9"/><path d="M4 6h8M9 3l3 3-3 3" fill="none" stroke="#a9a9a9"/></svg></span>
        <span>BUY</span>
      </div>
    </article>
  </div>
  <div class="load-more">Load more products</div>

  <h2 class="section-title second">Products from other Users</h2>
  <div class="product-grid second">
    <article class="product-card">
      <div class="product-photo" role="img" aria-label="Photo of a spool of white twine" style="background:#dcd9d4"></div>
      <div class="product-name">Special wood pencils</div>
      <div class="followers">
        <div class="follower"><div class="avatar" role="img" aria-label="Follower photo" style="background:#5e5247"></div><div class="follower-name">Marek</div></div>
        <div class="follower"><div class="avatar" role="img" aria-label="Follower photo" style="background:#6f665d"></div><div class="follower-name">Tobin</div></div>
        <div class="follower"><div class="avatar" role="img" aria-label="Follower photo" style="background:#5f6b78"></div><div class="follower-name">Ilse</div></div>
        <div class="more-count">+10</div>
      </div>
    </article>
    <article class="product-card">
      <div class="product-photo" role="img" aria-label="Photo of white lace socks and shoes" style="background:#b9b7b3"></div>
      <div class="product-name">Modern dress with laces</div>
      <div class="followers">
        <div class="follower"><div class="avatar" role="img" aria-label="Follower photo" style="background:#5e5247"></div><div class="follower-name">Marek</div></div>
        <div class="follower"><div class="avatar" role="img" aria-label="Follower photo" style="background:#6f665d"></div><div class="follower-name">Tobin</div></div>
        <div class="follower"><div class="avatar" role="img" aria-label="Follower photo" style="background:#5f6b78"></div><div class="follower-name">Ilse</div></div>
        <div class="more-count">+10</div>
      </div>
    </article>
    <article class="product-card">
      <div class="product-photo" role="img" aria-label="Photo of a locket beside a white cup" style="background:#d2d2cf"></div>
      <div class="product-name">Set of pilows</div>
      <div class="followers">
        <div class="follower"><div class="avatar" role="img" aria-label="Follower photo" style="background:#5e5247"></div><div class="follower-name">Marek</div></div>
        <div class="follower"><div class="avatar" role="img" aria-label="Follower photo" style="background:#6f665d"></div><div class="follower-name">Tobin</div></div>
        <div class="follower"><div class="avatar" role="img" aria-label="Follower photo" style="background:#5f6b78"></div><div class="follower-name">Ilse</div></div>
        <div class="more-count">+10</div>
      </div>
    </article>
    <article class="product-card">
      <div class="product-photo" role="img" aria-label="Photo of a white stone bead bracelet" style="background:#e9e3d9"></div>
      <div class="product-name">Gold plated vintage breclet</div>
      <div class="followers">
        <div class="follower"><div class="avatar" role="img" aria-label="Follower photo" style="background:#5e5247"></div><div class="follower-name">Marek</div></div>
        <div class="follower"><div class="avatar" role="img" aria-label="Follower photo" style="background:#6f665d"></div><div class="follower-name">Tobin</div></div>
        <div class="follower"><div class="avatar" role="img" aria-label="Follower photo" style="background:#5f6b78"></div><div class="follower-name">Ilse</div></div>
        <div class="more-count">+10</div>
      </div>
    </article>
  </div>
  <div class="load-more second">Load more products</div>

  <footer class="site-footer">© 2013 Bargo Finch<span class="divider">|</span><a href="#">Disclaimer</a></footer>
</div>
</body>
</html>
```